Redesign of the iOS/apk app vorbu.

I have an app that need a new more vibrant modern design, I already have a draft in jpg but I need it in psd and some minor animation very simple.

We also need a high high end design(r) for Kxxxx Bxx, play with the D and S, think Maren Trovelle, Pavone, Tormi, Odile Brancart Nemours and so on. Also need pattern and more. it needs to work as small, big letters, signs, clothes, sunglasses, coffee cups, plates, basically on everything.

Sunglasses

```html
<!DOCTYPE html>
<html lang="en">
<head>
<meta charset="utf-8">
<title>vorbu – game board</title>
<link href="https://fonts.googleapis.com/css2?family=Arimo:wght@400;700&display=swap" rel="stylesheet">
<style>
  :root {
    --bg-dark: #151515;
    --header-metal: #2a2a2a;
    --btn-top: #9a9a9a;
    --btn-bottom: #3c3c3c;
    --text-light: #ffffff;
    --square-light: #e6e6e6;
    --square-dark: #8c8c8c;
    --panel-edge: #5a5a5a;
    --die-grey: #8d8d8d;
    --die-yellow: #e6c51c;
    --die-yellow-dark: #b89a0b;
    --piece-white: #efe9da;
    --piece-white-edge: #9b907a;
    --piece-black: #1c1c1c;
    --piece-black-edge: #555555;
    --pass-grey: #6e6e6e;
    --surrender-red: #d8343a;
    --roll-green: #27c21f;
    --roll-green-dark: #137b10;
    --roll-text: #0f5e0c;
  }
  * { box-sizing: border-box; margin: 0; padding: 0; }
  html, body { width: 800px; height: 1200px; overflow: hidden; background: var(--bg-dark); font-family: "Arimo", Arial, sans-serif; }
  .app { position: relative; width: 800px; height: 1200px; }
  .sprite { position: absolute; width: 0; height: 0; }

  .header { position: absolute; left: 0; top: 0; width: 800px; height: 116px;
    background: radial-gradient(circle, #3a3a3a 1px, transparent 1.5px) 0 0/5px 5px, var(--header-metal);
    border-bottom: 4px solid #0c0c0c; }
  .header-button { position: absolute; top: 30px; width: 244px; height: 62px; border-radius: 31px;
    background: linear-gradient(var(--btn-top), #6a6a6a 50%, var(--btn-bottom));
    border: 2px solid #1a1a1a; color: var(--text-light); font-weight: 700; font-size: 24px;
    display: flex; align-items: center; justify-content: center; text-shadow: 0 1px 2px #000; }
  .header-button--rules { left: 18px; }
  .header-button--stats { right: 16px; }
  .app-title { position: absolute; left: 0; right: 0; top: 26px; text-align: center;
    color: var(--text-light); font-size: 60px; font-weight: 700; line-height: 70px; letter-spacing: 1px; }

  .board { position: absolute; left: 0; top: 122px; width: 800px; height: 800px;
    display: grid; grid-template-columns: repeat(8, 100px); grid-template-rows: repeat(8, 100px); }
  .square { position: relative; background: linear-gradient(135deg, var(--square-light), #cfcfcf); }
  .square--dark { background: linear-gradient(135deg, #9a9a9a, #7a7a7a); }

  .piece { position: absolute; left: 25px; bottom: 4px; width: 50px; height: 84px; }
  .piece--white { color: var(--piece-white); stroke: var(--piece-white-edge); }
  .piece--black { color: var(--piece-black); stroke: var(--piece-black-edge); }
  .piece use { fill: currentColor; stroke-width: 1.2; }

  .controls { position: absolute; left: 0; top: 924px; width: 800px; height: 276px; background: #2a2a2a; }
  .tray { position: absolute; left: 8px; top: 8px; width: 454px; height: 262px;
    background: linear-gradient(#d8d8d8, #b4b4b4); border-radius: 10px; border: 2px solid var(--panel-edge); }
  .dice-row { position: absolute; left: 10px; top: 12px; width: 430px; height: 140px;
    border: 2px solid #444; border-radius: 18px; background: linear-gradient(#cfcfcf, #a9a9a9);
    display: flex; justify-content: space-around; align-items: center; padding: 0 6px; }
  .die { position: relative; width: 118px; height: 106px; border-radius: 16px; border: 3px solid #111; }
  .die--neutral { background: linear-gradient(135deg, #b5b5b5, var(--die-grey)); }
  .die--active { background: linear-gradient(135deg, #f3dc4b, var(--die-yellow) 60%, var(--die-yellow-dark)); }
  .die .piece { left: 33px; bottom: 10px; width: 46px; height: 80px; }
  .action { position: absolute; top: 170px; height: 84px; border-radius: 10px; border: 2px solid #333;
    color: var(--text-light); font-size: 28px; font-weight: 700; text-shadow: 0 1px 2px #000;
    display: flex; align-items: center; justify-content: center; }
  .action--pass { left: 10px; width: 210px; background: linear-gradient(#8a8a8a, var(--pass-grey) 50%, #4a4a4a); }
  .action--surrender { left: 232px; width: 210px; background: linear-gradient(#ee5a5f, var(--surrender-red) 50%, #a51e23); }
  .divider { position: absolute; left: 466px; top: 8px; width: 68px; height: 262px;
    background: repeating-linear-gradient(45deg, #6a6a6a 0 2px, #2e2e2e 2px 5px); }
  .roll-panel { position: absolute; left: 538px; top: 8px; width: 254px; height: 262px;
    background: linear-gradient(#d0d0d0, #a8a8a8); border: 2px solid var(--panel-edge); border-radius: 10px; }
  .roll-button { position: absolute; left: 14px; top: 16px; width: 224px; height: 228px; border-radius: 14px;
    background: linear-gradient(160deg, #5fe052, var(--roll-green) 50%, var(--roll-green-dark));
    border: 3px solid #0c4a09; display: flex; flex-direction: column; align-items: center; }
  .roll-lines { margin-top: 22px; width: 96px; height: 26px;
    background: repeating-linear-gradient(var(--roll-text) 0 4px, transparent 4px 10px); opacity: .7; }
  .roll-label { margin-top: 8px; color: var(--roll-text); font-size: 56px; font-weight: 700;
    line-height: 52px; text-align: center; }
</style>
</head>
<body>
<svg class="sprite" aria-hidden="true">
  <defs>
    <symbol id="pawn" viewBox="0 0 40 80">
      <path d="M4 78 v-6 q0-3 4-4 h24 q4 1 4 4 v6z M9 68 Q15 50 16 38 h8 Q25 50 31 68z M11 33 h18 v5 h-18z"/>
      <circle cx="20" cy="23" r="9"/>
    </symbol>
    <symbol id="rook" viewBox="0 0 40 80">
      <path d="M4 78 v-6 q0-3 4-4 h24 q4 1 4 4 v6z M10 68 L13 30 h14 L30 68z M8 10 h6 v5 h3 v-5 h6 v5 h3 v-5 h6 v20 h-24z"/>
    </symbol>
    <symbol id="knight" viewBox="0 0 40 80">
      <path d="M4 78 v-6 q0-3 4-4 h24 q4 1 4 4 v6z M9 68 Q11 56 19 46 Q13 48 9 44 Q5 39 9 33 L17 22 L18 12 L23 17 Q34 22 33 42 Q32 56 32 68z"/>
    </symbol>
    <symbol id="bishop" viewBox="0 0 40 80">
      <path d="M4 78 v-6 q0-3 4-4 h24 q4 1 4 4 v6z M11 68 Q16 52 17 42 h6 Q24 52 29 68z M11 37 h18 v5 h-18z"/>
      <ellipse cx="20" cy="26" rx="8" ry="11"/>
      <circle cx="20" cy="12" r="3"/>
    </symbol>
    <symbol id="queen" viewBox="0 0 40 80">
      <path d="M4 78 v-6 q0-3 4-4 h24 q4 1 4 4 v6z M10 68 Q16 48 16 32 h8 Q24 48 30 68z M10 28 h20 v5 h-20z M9 12 L13 28 h14 L31 12 L25 20 L20 9 L15 20z"/>
      <circle cx="9" cy="11" r="2.5"/><circle cx="20" cy="7" r="2.5"/><circle cx="31" cy="11" r="2.5"/>
    </symbol>
    <symbol id="king" viewBox="0 0 40 80">
      <path d="M4 78 v-6 q0-3 4-4 h24 q4 1 4 4 v6z M10 68 Q16 48 16 32 h8 Q24 48 30 68z M10 28 h20 v5 h-20z M11 16 Q20 11 29 16 L26 28 h-12z M18 1 h4 v4 h4 v4 h-4 v5 h-4 v-5 h-4 v-4 h4z"/>
    </symbol>
  </defs>
</svg>

<div class="app">
  <header class="header">
    <div class="header-button header-button--rules">Rules</div>
    <h1 class="app-title">vorbu</h1>
    <div class="header-button header-button--stats">Stats</div>
  </header>

  <main class="board">
    <div class="square square--dark"></div>
    <div class="square"><svg class="piece piece--white" role="img" aria-label="White knight"><use href="#knight"/></svg></div>
    <div class="square square--dark"><svg class="piece piece--white" role="img" aria-label="White rook"><use href="#rook"/></svg></div>
    <div class="square"></div>
    <div class="square square--dark"><svg class="piece piece--white" role="img" aria-label="White king"><use href="#king"/></svg></div>
    <div class="square"></div><div class="square square--dark"></div><div class="square"></div>

    <div class="square"><svg class="piece piece--white" role="img" aria-label="White pawn"><use href="#pawn"/></svg></div>
    <div class="square square--dark"></div>
    <div class="square"><svg class="piece piece--white" role="img" aria-label="White bishop"><use href="#bishop"/></svg></div>
    <div class="square square--dark"></div><div class="square"></div><div class="square square--dark"></div><div class="square"></div><div class="square square--dark"></div>

    <div class="square square--dark"></div><div class="square"></div><div class="square square--dark"></div>
    <div class="square"><svg class="piece piece--white" role="img" aria-label="White queen"><use href="#queen"/></svg></div>
    <div class="square square--dark"></div><div class="square"></div><div class="square square--dark"></div><div class="square"></div>

    <div class="square"></div><div class="square square--dark"></div><div class="square"></div><div class="square square--dark"></div><div class="square"></div><div class="square square--dark"></div><div class="square"></div><div class="square square--dark"></div>
    <div class="square square--dark"></div><div class="square"></div><div class="square square--dark"></div><div class="square"></div><div class="square square--dark"></div><div class="square"></div><div class="square square--dark"></div><div class="square"></div>
    <div class="square"></div><div class="square square--dark"></div><div class="square"></div><div class="square square--dark"></div><div class="square"></div><div class="square square--dark"></div><div class="square"></div><div class="square square--dark"></div>

    <div class="square square--dark"></div>
    <div class="square"><svg class="piece piece--black" role="img" aria-label="Black pawn"><use href="#pawn"/></svg></div>
    <div class="square square--dark"></div><div class="square"></div><div class="square square--dark"></div><div class="square"></div><div class="square square--dark"></div><div class="square"></div>

    <div class="square"><svg class="piece piece--black" role="img" aria-label="Black rook"><use href="#rook"/></svg></div>
    <div class="square square--dark"></div>
    <div class="square"><svg class="piece piece--black" role="img" aria-label="Black bishop"><use href="#bishop"/></svg></div>
    <div class="square square--dark"><svg class="piece piece--black" role="img" aria-label="Black queen"><use href="#queen"/></svg></div>
    <div class="square"></div><div class="square square--dark"></div><div class="square"></div><div class="square square--dark"></div>
  </main>

  <section class="controls">
    <div class="tray">
      <div class="dice-row">
        <div class="die die--neutral"><svg class="piece piece--white" role="img" aria-label="Die face: white bishop"><use href="#bishop"/></svg></div>
        <div class="die die--active"><svg class="piece piece--black" role="img" aria-label="Die face: black knight"><use href="#knight"/></svg></div>
        <div class="die die--active"><svg class="piece piece--black" role="img" aria-label="Die face: black king"><use href="#king"/></svg></div>
      </div>
      <div class="action action--pass">pass</div>
      <div class="action action--surrender">surrender</div>
    </div>
    <div class="divider"></div>
    <div class="roll-panel">
      <div class="roll-button">
        <div class="roll-lines"></div>
        <div class="roll-label">ROLL<br>DICE</div>
      </div>
    </div>
  </section>
</div>
</body>
</html>
```